Brivoza banner and eDM design

We need banner ads and an eDM header to promote Brivoza.com.au (not currently live but logo and site design complete).

Banners should ideally be in flash with back-up gifs but we would be open to just animated gifs as well.

Banner sizes to be delivered are:
300x250
729x90
468x60
160x600

Best to keep banner file size under 25kb if possible (based on standard publisher specs)

For the eDM header, it should be around:
600 wide x
150-200 high

The advertising role is to promote the websites services which are related to making HR easy for small business owners - specifically relating to recruitment, induction, engagement and employee exit. I'll attach more details on this.

Target Market(s)

Small and medium business owners - slightly male skew

Industry/Entity Type

Small Business

Requirements
Must have
• Must match the look and feel and colour palette of the logo and website design that will be attached to this brief.

Must look professional

Must follow the copy guide for the frames as outlined in the attachment - there are 2 options for frame 3 listed. I'd like to get 2 sets of banners developed to cover both options.

Must have clear call-to-action
Nice to have
• Nice to have sophisticated animation if possible

I've added two potential images that could be used - either could be used to illustrate the 'Save time and improve results' line -
one focused on finding the right person
one is focused on improving results through a team

You could potentially use a screen grab of the site homepage in the design too - but only if eligible since none of the copy on it is finalised.

```html
<!DOCTYPE html>
<html lang="en">
<head>
<meta charset="utf-8">
<title>Brivoza banner set</title>
<link rel="stylesheet" href="https://fonts.googleapis.com/css2?family=Source+Sans+3:wght@600;700&display=swap">
<style>
  :root {
    --page-light: #f7f7f7;
    --page-dark: #dcdcdc;
    --banner-bg: #ffffff;
    --banner-edge: #1d2a4a;
    --brand-blue: #3f6fa6;
    --band-blue: #1670b8;
    --ink-grey: #8b8f98;
    --cta-top: #ffab4a;
    --cta-bottom: #ee7412;
    --cta-edge: #c85f0c;
    --art-light: #e9eef5;
    --art-mid: #c9d2dc;
    --art-blue: #5aa7e6;
  }
  * { box-sizing: border-box; margin: 0; padding: 0; }
  html, body { width: 960px; height: 1200px; overflow: hidden; }
  body {
    font-family: "Source Sans 3", "Myriad Pro", Arial, sans-serif;
    background: radial-gradient(ellipse at 50% 45%, var(--page-light) 0%, #efefef 50%, var(--page-dark) 100%);
  }
  .sheet { position: relative; width: 960px; height: 1200px; }
  .banner {
    position: absolute;
    left: 102px;
    width: 720px;
    height: 180px;
    background: var(--banner-bg);
    border: 1px solid var(--banner-edge);
    box-shadow: 3px 6px 8px rgba(0,0,0,0.28);
    overflow: hidden;
  }
  .banner--team { top: 34px; }
  .banner--results { top: 275px; }
  .banner--guides { top: 515px; }
  .banner--free { top: 756px; }
  .banner--header { top: 996px; }

  .brand {
    position: absolute;
    display: flex;
    align-items: center;
    gap: 8px;
    color: var(--brand-blue);
    font-weight: 700;
    letter-spacing: -0.5px;
  }
  .brand__dot { border-radius: 50%; background: var(--brand-blue); flex: none; }
  .brand--small { left: 484px; top: 38px; font-size: 42px; line-height: 48px; }
  .brand--small .brand__dot { width: 40px; height: 40px; }
  .brand--large { left: 26px; top: 20px; font-size: 86px; line-height: 100px; gap: 14px; }
  .brand--large .brand__dot { width: 86px; height: 86px; }

  .cta {
    position: absolute;
    left: 488px;
    top: 102px;
    width: 206px;
    height: 40px;
    border-radius: 5px;
    border: 1px solid var(--cta-edge);
    background: linear-gradient(var(--cta-top), var(--cta-bottom));
    box-shadow: 2px 3px 4px rgba(0,0,0,0.35);
    color: #ffffff;
    font-weight: 700;
    font-size: 22px;
    line-height: 38px;
    text-align: center;
  }
  .banner--header .cta { left: 490px; top: 55px; }

  .artwork {
    position: absolute;
    background: linear-gradient(100deg, var(--art-light) 0%, var(--art-mid) 55%, var(--art-blue) 100%);
    border-radius: 4px;
  }
  .banner--team .artwork { left: 126px; top: 18px; width: 340px; height: 160px; }
  .banner--results .artwork { left: 282px; top: 14px; width: 186px; height: 164px; }

  .headline { position: absolute; font-weight: 700; line-height: 1; }
  .headline--save { left: 44px; top: 38px; }
  .headline__big { display: block; color: var(--brand-blue); font-size: 40px; }
  .headline__small { display: block; color: var(--ink-grey); font-size: 26px; margin: 2px 0 4px; }

  .guides { position: absolute; left: 26px; top: 22px; font-weight: 700; }
  .guides__lead { display: flex; align-items: center; gap: 10px; font-size: 25px; color: var(--ink-grey); }
  .guides__lead strong { color: var(--brand-blue); }
  .guides__marks { display: flex; gap: 4px; }
  .guides__marks span { width: 15px; height: 15px; background: var(--brand-blue); display: block; }
  .guides__list { list-style: none; margin: 4px 0 0 72px; }
  .guides__list li { font-size: 28px; line-height: 40px; color: var(--brand-blue); }
  .guides__list .muted { color: var(--ink-grey); }

  .offer { position: absolute; left: 30px; top: 50px; width: 420px; text-align: center; font-weight: 700; }
  .offer__line1 { font-size: 25px; color: var(--ink-grey); line-height: 44px; }
  .offer__line1 strong { color: var(--brand-blue); font-size: 42px; vertical-align: -3px; }
  .offer__line2 { font-size: 32px; color: var(--brand-blue); line-height: 38px; }

  .tagline-band {
    position: absolute;
    left: 0; right: 0; bottom: 0;
    height: 48px;
    background: var(--band-blue);
    color: #ffffff;
    font-weight: 700;
    font-size: 31px;
    letter-spacing: 2px;
    line-height: 48px;
    text-align: center;
  }
</style>
</head>
<body>
<main class="sheet">

  <section class="banner banner--team">
    <div class="artwork" role="img" aria-label="Illustration of a team of figures pulling a rope along a rising blue arrow"></div>
    <div class="brand brand--small"><span class="brand__dot"></span>Brivoza</div>
    <div class="cta">Find out more</div>
  </section>

  <section class="banner banner--results">
    <h2 class="headline headline--save">
      <span class="headline__big">Save time</span>
      <span class="headline__small">and improve</span>
      <span class="headline__big">RESULTS</span>
    </h2>
    <div class="artwork" role="img" aria-label="Illustration of a team pulling a rope up a rising blue arrow"></div>
    <div class="brand brand--small"><span class="brand__dot"></span>Brivoza</div>
    <div class="cta">Find out more</div>
  </section>

  <section class="banner banner--guides">
    <div class="guides">
      <p class="guides__lead">
        <span class="guides__marks"><span></span><span></span><span></span></span>
        <span>with <strong>How To Guides on:</strong></span>
      </p>
      <ul class="guides__list">
        <li>Recruitment</li>
        <li>Induction</li>
        <li>Exit <span class="muted">and more</span></li>
      </ul>
    </div>
    <div class="brand brand--small"><span class="brand__dot"></span>Brivoza</div>
    <div class="cta">Find out more</div>
  </section>

  <section class="banner banner--free">
    <div class="offer">
      <p class="offer__line1">Featuring <strong>FREE</strong> instructional</p>
      <p class="offer__line2">HR videos and articles</p>
    </div>
    <div class="brand brand--small"><span class="brand__dot"></span>Brivoza</div>
    <div class="cta">Find out more</div>
  </section>

  <section class="banner banner--header">
    <div class="brand brand--large"><span class="brand__dot"></span>Brivoza</div>
    <div class="cta">Find out more</div>
    <p class="tagline-band">Easy end to end HR solutions</p>
  </section>

</main>
</body>
</html>
```